Law Enforcement Services Leader Seeking Graphic Design for 2 Roll Up Banners

Bluecrest Shift Group( the leader in police administrative services) needs a graphic designer to develop two separate graphics for a pair of 33" edge retractable roll-up banners to complete our trade show booth display. Please reference our website at www.bluecrestshiftgroup.example as well as the uploaded files to get a feel for our branding.

```html
<!DOCTYPE html>
<html lang="en">
<head>
<meta charset="utf-8">
<title>Bluecrest Shift Group – Roll-Up Banners</title>
<link rel="stylesheet" href="https://fonts.googleapis.com/css2?family=Montserrat:wght@400;500;600&family=Rajdhani:wght@500;600&display=swap">
<style>
  :root{
    --stage-top:#9a9a9a;
    --stage-bottom:#2e2e2e;
    --navy-deep:#04163a;
    --navy:#0a2a5c;
    --blue-band:#0b9be0;
    --blue-band-dark:#0680c4;
    --accent:#27b8f5;
    --white:#ffffff;
  }
  *{margin:0;padding:0;box-sizing:border-box}
  html,body{width:1200px;height:686px;overflow:hidden}
  body{
    background:linear-gradient(180deg,var(--stage-top),var(--stage-bottom));
    font-family:"Montserrat",sans-serif;
    color:var(--white);
    display:flex;align-items:center;justify-content:center;gap:48px;
  }
  .banner{
    position:relative;width:262px;height:620px;overflow:hidden;
    background:var(--navy-deep);
    box-shadow:0 8px 24px rgba(0,0,0,.45);
  }
  .banner__photo{
    position:absolute;left:0;top:0;width:100%;height:300px;
    background:linear-gradient(160deg,#12386f 0%,#0a2550 45%,#051a40 100%);
  }
  .banner__shapes{position:absolute;inset:0}
  .brand{
    position:absolute;top:34px;left:0;width:100%;
    display:flex;align-items:center;justify-content:center;gap:8px;
  }
  .brand__dot{width:14px;height:14px;border-radius:50%;background:var(--white)}
  .brand__name{
    font-weight:500;font-size:13px;letter-spacing:2.4px;text-transform:uppercase;
    line-height:1.25;text-align:center;color:var(--white);
  }
  .headline{
    position:absolute;left:32px;top:128px;padding-left:12px;
    border-left:2px solid var(--accent);
    font-family:"Rajdhani",sans-serif;font-weight:500;line-height:1.18;
  }
  .headline--caps{font-size:20px;text-transform:uppercase;letter-spacing:.3px}
  .headline--title{font-size:17px;left:38px;top:114px}
  .headline__accent{color:var(--accent)}
  .features{position:absolute;left:0;width:100%;list-style:none}
  .feature{display:flex;align-items:center;margin-bottom:11px}
  .feature__icon{
    flex:none;width:38px;height:38px;margin-left:35px;border-radius:50%;
    background:var(--white);border:2px solid var(--accent);
    box-shadow:0 0 0 3px rgba(255,255,255,.25),3px 3px 6px rgba(0,0,0,.25);
    display:flex;align-items:center;justify-content:center;
  }
  .feature__icon svg{width:22px;height:22px;fill:none;stroke:var(--navy);stroke-width:1.5;stroke-linecap:round;stroke-linejoin:round}
  .feature__text{
    margin-left:12px;padding-left:8px;border-left:1px solid rgba(255,255,255,.8);
    font-size:9.4px;line-height:1.3;max-width:160px;
  }
  .url{
    position:absolute;left:0;bottom:28px;width:100%;text-align:center;
    font-weight:600;font-size:10.5px;letter-spacing:.2px;
  }
</style>
</head>
<body>

<!-- Banner one -->
<section class="banner">
  <div class="banner__photo" role="img" aria-label="Darkened blue-toned photo of a team of professionals meeting around a table"></div>
  <svg class="banner__shapes" viewBox="0 0 262 620" aria-hidden="true">
    <polygon points="0,280 262,237 262,260 0,300" fill="#0878c0"/>
    <polygon points="0,286 262,246 262,519 0,564" fill="var(--blue-band)"/>
    <polygon points="0,420 262,330 262,519 0,564" fill="var(--blue-band-dark)" opacity=".35"/>
    <polygon points="0,552 262,512 262,620 0,620" fill="var(--navy)"/>
    <polygon points="0,564 262,519 262,620 0,620" fill="var(--navy-deep)"/>
  </svg>
  <div class="brand"><span class="brand__dot"></span><span class="brand__name">Bluecrest<br>Shift Group</span></div>
  <h1 class="headline headline--caps">Extra Duty<br>Support For<br><span class="headline__accent">Law Enforcement<br>Agencies</span></h1>
  <ul class="features" style="top:293px">
    <li class="feature"><span class="feature__icon"><svg viewBox="0 0 24 24"><rect x="9" y="3" width="11" height="15" rx="1"/><path d="M12 7h5M12 10h5M12 13h3"/><circle cx="7" cy="16" r="3"/><circle cx="7" cy="16" r="1"/></svg></span><p class="feature__text">Ability to handle nearly any detail assignment process including combinations of multiple methods</p></li>
    <li class="feature"><span class="feature__icon"><svg viewBox="0 0 24 24"><path d="M5 13a7 7 0 0 1 14 0"/><rect x="3" y="13" width="4" height="6" rx="1"/><rect x="17" y="13" width="4" height="6" rx="1"/><path d="M19 19q0 2-4 2"/></svg></span><p class="feature__text">Account Team approach with 24/7/365 insourced coverage of phone calls</p></li>
    <li class="feature"><span class="feature__icon"><svg viewBox="0 0 24 24"><circle cx="12" cy="5" r="2"/><path d="M12 7v5M5 12h14M5 12v4M12 12v4M19 12v4"/><circle cx="5" cy="18" r="2"/><circle cx="12" cy="18" r="2"/><circle cx="19" cy="18" r="2"/></svg></span><p class="feature__text">Multiple operations centers with complete failover and disaster recovery</p></li>
    <li class="feature"><span class="feature__icon"><svg viewBox="0 0 24 24"><rect x="4" y="4" width="12" height="17" rx="1"/><path d="M8 3h4v3H8zM7 10l1 1 2-2M7 15l1 1 2-2"/><path d="M17 12l4 1.5v3c0 2-2 3.5-4 4.5-2-1-4-2.5-4-4.5v-3z"/></svg></span><p class="feature__text">Industry-leading, flexible liability and worker's comp insurance which is primary to yours</p></li>
  </ul>
  <p class="url">www.bluecrestshiftgroup.example</p>
</section>

<!-- Banner two -->
<section class="banner">
  <div class="banner__photo" role="img" aria-label="Darkened blue-toned photo of colleagues collaborating at a desk"></div>
  <svg class="banner__shapes" viewBox="0 0 262 620" aria-hidden="true">
    <polygon points="0,237 262,280 262,300 0,260" fill="#0878c0"/>
    <polygon points="0,246 262,286 262,564 0,519" fill="var(--blue-band)"/>
    <polygon points="0,330 262,420 262,564 0,519" fill="var(--blue-band-dark)" opacity=".35"/>
    <polygon points="0,512 262,552 262,620 0,620" fill="var(--navy)"/>
    <polygon points="0,519 262,564 262,620 0,620" fill="var(--navy-deep)"/>
  </svg>
  <div class="brand"><span class="brand__dot"></span><span class="brand__name">Bluecrest<br>Shift Group</span></div>
  <h2 class="headline headline--title">We Administer<br>Extra Duty Programs<br>So You Can Focus On<br>The <span class="headline__accent">Safety Of<br>Your Citizens</span></h2>
  <ul class="features" style="top:296px">
    <li class="feature"><span class="feature__icon"><svg viewBox="0 0 24 24"><rect x="8" y="3" width="8" height="9" rx="3"/><path d="M6 11v2h12v-2M12 13v4M7 21l5-4 5 4M5 9v3M19 9v3"/></svg></span><p class="feature__text">We're more than an app. We're a fully-staffed service provider leveraging state-of-the-art technology.</p></li>
    <li class="feature"><span class="feature__icon"><svg viewBox="0 0 24 24"><path d="M2 9l4-2 6 3 6-3 4 2M6 7l-3 6 3 3M18 7l3 6-3 3M9 12l3 3 3-3M8 15l2 2M11 17l1 1"/></svg></span><p class="feature__text">There's no conflict of interest. We work directly for your agency, not your vendors.</p></li>
    <li class="feature"><span class="feature__icon"><svg viewBox="0 0 24 24"><rect x="3" y="4" width="18" height="12" rx="1"/><path d="M9 20h6M12 16v4"/><circle cx="9.5" cy="10" r="2"/><circle cx="14.5" cy="10" r="2"/></svg></span><p class="feature__text">We provide on-duty software as well as API integration into other on-duty software packages</p></li>
    <li class="feature"><span class="feature__icon"><svg viewBox="0 0 24 24"><path d="M9 4l6 6M7 6l4-4 6 6-4 4zM11 10l-7 7 2 2 7-7"/><rect x="12" y="18" width="9" height="3" rx="1"/></svg></span><p class="feature__text">Our team consists of several law enforcement and operational leaders</p></li>
  </ul>
  <p class="url">www.bluecrestshiftgroup.example</p>
</section>

</body>
</html>
```